Zielgruppe
Hausarztpraxis Dr. Wildhagen
Patientenbetreuung / Junge Patienten
Aufgabenstellung
Bitte Mit dem Praxis Logo. Gern auch ein Foto aus der Praxis. In den Farben der Praxis Weiß-Magenta-Grau
Es soll kein Newsletter an sich werden, sondern eine Email die die Patienten nach Ihrem Besuch in der Praxis bekommen. Dort soll dann die Suchflixseite verlinkt sein mit einem Button zum bewerten!

```html
<!DOCTYPE html>
<html lang="de">
<head>
<meta charset="utf-8">
<title>Bewertungs-E-Mail – Hausarztpraxis Dr. Wildhagen</title>
<link href="https://fonts.googleapis.com/css2?family=Open+Sans:wght@400;600;700&display=swap" rel="stylesheet">
<style>
  :root {
    --magenta: #c41a59;
    --magenta-soft: rgba(200, 40, 100, 0.88);
    --pink-light: #ef6a9c;
    --grey-text: #5a5a5a;
    --white: #ffffff;
  }
  * { margin: 0; padding: 0; box-sizing: border-box; }
  html, body { width: 940px; height: 1200px; overflow: hidden; background: var(--white); }
  body { position: relative; font-family: "Open Sans", sans-serif; color: var(--grey-text); }

  .brand {
    position: absolute; top: 20px; left: 0; width: 940px;
    display: flex; flex-direction: column; align-items: center; gap: 16px;
  }
  .brand-mark {
    width: 50px; height: 50px; border-radius: 50%;
    border: 4px solid var(--magenta);
  }
  .brand-name {
    font-size: 13px; font-weight: 600; color: var(--magenta);
    letter-spacing: 0.05em; text-transform: uppercase;
  }

  .hero-photo {
    position: absolute; top: 143px; left: 0; width: 940px; height: 263px;
    background:
      linear-gradient(180deg, rgba(255,255,255,0.35) 0%, rgba(255,255,255,0) 60%, rgba(120,120,130,0.18) 100%),
      linear-gradient(90deg, #e9e8e6 0%, #f4f4f3 20%, #ededeb 40%, #cdc6b8 55%, #a89b85 62%, #cfcbc5 72%, #bdb9b4 85%, #d6d4d1 100%);
  }

  .hero-card {
    position: absolute; top: 337px; left: 204px; width: 532px; height: 119px;
    background: var(--magenta-soft); color: var(--white); text-align: center;
  }
  .hero-title { margin-top: 26px; font-size: 26px; font-weight: 400; line-height: 1.2; }
  .hero-subtitle { margin-top: 7px; font-size: 12px; }

  .message {
    position: absolute; top: 502px; left: 204px; width: 532px;
    text-align: center; font-size: 11.5px; line-height: 15.7px;
  }
  .message p { margin-bottom: 15.6px; }

  .cta {
    position: absolute; top: 667px; left: 204px; width: 532px; height: 32px;
    border-radius: 16px; background: var(--magenta);
    display: flex; align-items: center; justify-content: center;
    color: var(--white); font-size: 11px; text-decoration: underline;
  }

  .closing {
    position: absolute; top: 722px; left: 200px; width: 540px;
    text-align: center; font-size: 11.5px; line-height: 15.7px;
  }
  .closing p { margin-bottom: 15.6px; }
  .phone { color: var(--magenta); font-weight: 700; }

  .review-illustration {
    position: absolute; top: 886px; left: 316px; width: 332px; height: 224px;
    border-radius: 14px;
    background:
      radial-gradient(ellipse 70% 60% at 50% 55%, #f7f3f5 0%, #f7f3f5 25%, rgba(240,122,168,0) 45%),
      radial-gradient(ellipse 60% 70% at 50% 45%, #ef73a3 0%, #e0588f 55%, rgba(255,255,255,0) 100%);
  }

  .footer-accent { position: absolute; top: 1166px; left: 0; width: 940px; height: 9px; background: var(--pink-light); }
  .footer {
    position: absolute; top: 1175px; left: 0; width: 940px; height: 25px;
    background: var(--magenta); color: var(--white);
    font-size: 11px; text-align: center; line-height: 25px;
  }
</style>
</head>
<body>
  <header class="brand">
    <div class="brand-mark"></div>
    <div class="brand-name">Hausarztpraxis Dr. Wildhagen</div>
  </header>

  <div class="hero-photo" role="img" aria-label="Foto des hellen Wartebereichs der Praxis mit weißen Stühlen, Bambusdekoration und grauen Sesseln"></div>

  <section class="hero-card">
    <h1 class="hero-title">Ihre Meinung ist uns wichtig.</h1>
    <p class="hero-subtitle">Nehmen Sie sich kurz zeit und bewerten Sie uns auf Suchflix.</p>
  </section>

  <section class="message">
    <p>Hallo Frau/Herr....,</p>
    <p>wie war Ihre Erfahrung bei Dr. Med. Annika Wildhagen?</p>
    <p>Wir versuchen ständig, uns zu verbessern und freuen uns, wenn du uns dein Feedback mitteilen könntest. Es wäre toll, wenn du dir kurz die Zeit nimmst, eine Bewertung bei Suchflix zu schreiben, denn damit hilfst du uns und auch anderen Kunden uns zu finden.</p>
    <p>Um Ihre Bewertung zu schreiben und abzuschicken, genügt ein Klick!</p>
  </section>

  <a class="cta" href="#">Jetzt Hausarztpraxis Dr.Med.Annika Wildhagen bewerten</a>

  <section class="closing">
    <p>Vielen Dank im Voraus für deine Bewertung! Bei Fragen oder falls Sie uns erneut besuchen möchtest, stehen wir dir jederzeit gerne zur Verfügung!</p>
    <p>Rufen Sie uns an unter der <span class="phone">07000- 12 34</span>.</p>
    <p>Viele Grüße,<br>Ihre Hausarztpraxis</p>
  </section>

  <div class="review-illustration" role="img" aria-label="Illustration: Menschen vor einem Browserfenster mit Bewertungsaufruf und fünf Sternen, umgeben von Pflanzen"></div>

  <div class="footer-accent"></div>
  <footer class="footer">Impressum &nbsp;I Datenschutz I Unsere Praxis I Kontakt</footer>
</body>
</html>
```